依頼詳細
弊社がお客様にお渡ししているパンフレットに添えたいと思っております。白樺工房が使用している断熱材をわかりやすくお客様に伝えるためのチラシを作成したいと考えているため、炭化コルクの性能をわかりやすく伝わるように写真・イラストを使用しながら、お客様が興味を持っていただくようなチラシの作成をお願い致します。

◎加えていただきたい内容
タイトル:炭に包まれた内断熱のお家

1.炭化コルクの優れた5つの性能
①断熱性能(スペースシャトルの断熱材としても使用されていました。)
②防虫性能(スぺリンという物質が虫やダニを寄せ付けません。)
③防音性能(優れた防音性能と吸音性、衝撃吸収性により音の振動を遮ります。)
④調湿性能(空気中の余分な水分を吸収、乾燥時ははき出したりすることで、室内の結露やカビの発生を防ぎます。)
⑤消臭性能(多孔質な炭の効果で、ペット臭などの嫌なにおいを吸着消臭します。)
※わかりやすくなるようイラスト添えでお願い致します。

2.炭化コルク+漆喰でつくる「空気のおいしい家」
ベルタスホームの健康住宅
漆喰と炭の効果で24時間サラッとした空気か365日続きます。

ジメジメした雨の日も室内はカラッと調湿する100%
天然素材の断熱材「炭化コルク」
天井と壁に炭化コルクが入っていて、内断熱になっているため
夏涼しく、冬暖かい室内にしてくれます。
(一般的な住宅メーカーは、クレナライトと呼ばれる発泡スチロールのような断熱材を天井部分にしか使用していないのですが、ベルタスホームは、炭化コルクの断熱材を天井と日の当たる壁一面に貼っております。イラスト参考になるかと思いますので、実際の比較施工写真を添付いたします。

3.炭化コルクとは?
コルクの木の樹皮からできています。
高温で蒸し焼きにするとコルク自身のヤニで固形化するため、シックハウスの原因となる価格接着剤を使用しない、天然コルク100%の断熱材です。

4.使用していただきたいお家の画像
実際に施工したお家の内装の写真を使用していただきたい画像を添付いたしますので、ご確認宜しくお願い致します。

★重要★
炭化コルクの良さである内断熱と調湿効果が分かりやすいものになるようイラストを用いて作っていただけますようお願い申し上げます。

データをイラレとJPGで頂けますと幸いです。
何卒よろしくお願い申し上げます。
記載項目
ベルタスホーム/チラシ
サイズ
A4
ページ数
片面
希望イメージ
シンプル 複雑
単色 カラフル
暗い 明るい
日常 高級
遊び心 厳粛
未来的 伝統的
女性的 男性的
希望する色
黄・オレンジ系、茶系
納品ファイル
• 高解像度JPG (.jpg)
• イラストレーター形式 (.ai)
補足説明
縦のA4サイズで作成お願い致します。
ファイルに添付してあります写真と、サンプルを利用して作成してくださいますようお願い申し上げます。
■ 選んだ理由

弊社のイメージカラーであるオレンジをすっきりとまとめて配置されていた点、弊社の使用している断熱材をわかりやすい且つ、伝わりやすくデザインしていただいた点や、何度も修正依頼をさせていただいたのにも関わらず真摯に対応していただいた点に惹かれ選ばせていただきました。イラストも見た目が可愛らしく伝わる内容であった点が気に入りました。ありがとうございました。

■ 提案者全員のお礼・コメント

この度は、ベルタスホーム株式会社の断熱材チラシにご応募いただき、誠にありがとうございました。年末の忙しい時期にも関わらず皆様のアイディアをいただけたこと誠に感謝しております。多くの素晴らしいアイディアをいただいた中から選ぶことは、とても難しい作業でした。どれもベルタスホームの雰囲気にあったものばかりでこんなにも多くの良い作品に出合えたことを大変うれしく思います。また、ご依頼をさせて頂く際もご一緒にお仕事させて頂きたいと思いますので、何卒よろしくお願い申し上げます。誠にありがとうございました。

```html
<!DOCTYPE html>
<html lang="ja">
<head>
<meta charset="utf-8">
<title>炭に包まれた内断熱のお家｜ベルタスホーム</title>
<link rel="stylesheet" href="https://fonts.googleapis.com/css2?family=Noto+Sans+JP:wght@400;500;700;900&family=Noto+Serif+JP:wght@700;900&display=swap">
<style>
:root{
  --brown:#5b3a22;
  --brown-dark:#3e2716;
  --orange:#e8862a;
  --orange-soft:#f6b56a;
  --cream:#f7efe2;
  --white:#ffffff;
  --text:#3a2a1e;
}
*{box-sizing:border-box;margin:0;padding:0}
html,body{width:855px;height:1200px;overflow:hidden;background:#fff}
body{font-family:"Noto Sans JP",sans-serif;color:var(--text)}
.flyer{position:relative;width:855px;height:1200px;background:var(--cream);overflow:hidden}

/* hero */
.hero{position:absolute;left:0;top:0;width:855px;height:380px;
  background:linear-gradient(180deg,#c9a07a 0%,#e4c9a6 35%,#b98459 70%,#7a4e2f 100%)}
.brand-box{position:absolute;left:24px;top:18px;width:200px;height:92px;background:var(--white);
  border-radius:4px;padding:10px 12px;box-shadow:0 2px 6px rgba(0,0,0,.15)}
.brand-tag{font-size:10px;color:var(--brown);letter-spacing:.05em;white-space:nowrap}
.brand-name{display:flex;align-items:center;gap:6px;margin-top:8px;font-size:18px;font-weight:700;color:var(--brown);white-space:nowrap}
.brand-name .mark{width:14px;height:14px;background:var(--orange);flex:none}
.brand-sub{font-size:9px;color:var(--brown);margin-top:6px;letter-spacing:.08em;white-space:nowrap}
.hero-note{position:absolute;right:28px;top:22px;width:130px;font-size:12px;font-weight:700;color:var(--white);
  line-height:1.5;transform:rotate(-6deg);text-shadow:0 1px 3px rgba(0,0,0,.4)}
.title{position:absolute;left:0;top:50px;width:855px;text-align:center;font-family:"Noto Serif JP",serif;
  font-weight:900;color:var(--brown-dark);-webkit-text-stroke:6px var(--white);paint-order:stroke fill}
.title .kanji{display:block;font-size:160px;line-height:1}
.title .ni{position:absolute;left:505px;top:110px;font-size:54px;line-height:1}
.title .wrap{display:block;font-size:66px;line-height:1.05;margin-top:-18px}
.title .main{display:block;font-size:74px;line-height:1.1;color:var(--brown)}
.title .main em{font-style:normal;color:var(--orange)}

/* five points */
.points{position:absolute;left:22px;top:376px;width:811px;height:194px;background:var(--white);
  border-radius:8px;padding:10px 12px}
.points-head{text-align:center;font-size:23px;font-weight:900;color:var(--brown);line-height:1.3}
.points-head .num{font-size:34px;color:var(--orange)}
.point-row{display:flex;gap:10px;margin-top:6px}
.point{flex:1;text-align:center}
.point-label{display:inline-block;background:var(--orange);color:var(--white);font-size:11px;font-weight:700;
  padding:1px 10px;border-radius:10px}
.point-name{font-size:21px;font-weight:900;color:var(--brown);margin:2px 0 4px;line-height:1.3}
.point-text{font-size:10.5px;line-height:1.5;text-align:left;color:var(--text)}

/* air section */
.air-band{position:absolute;left:22px;top:580px;width:811px;height:36px;background:var(--brown);
  color:var(--white);font-size:21px;font-weight:900;text-align:center;line-height:36px;border-radius:4px}
.air-band em{font-style:normal;color:var(--orange-soft)}
.diagram{position:absolute;left:22px;top:628px;width:350px;height:220px;border-radius:6px;
  background:linear-gradient(135deg,#f3e3c8,#d9b98e 60%,#8a6a4c)}
.air-body{position:absolute;left:392px;top:628px;width:441px}
.air-lead{font-size:22px;font-weight:900;color:var(--brown);line-height:1.35}
.air-lead .hl{color:var(--orange)}
.air-text{margin-top:10px;font-size:12px;line-height:1.7}
.air-text b{color:var(--orange)}

/* bottom */
.bottom{position:absolute;left:22px;top:860px;width:811px;height:250px;display:flex;gap:10px}
.about{width:270px;background:var(--white);border:2px solid var(--orange);border-radius:6px;padding:10px}
.about h3{display:inline-block;background:var(--orange);color:var(--white);font-size:16px;font-weight:900;
  padding:2px 10px;border-radius:4px}
.about p{font-size:11px;line-height:1.65;margin-top:8px}
.about .photo{margin-top:8px;height:78px;border-radius:4px;background:linear-gradient(135deg,#3b2a20,#7a5a3e)}
.compare{flex:1;background:var(--white);border-radius:6px;padding:10px}
.compare h4{font-size:14px;font-weight:900;color:var(--white);background:var(--brown);padding:3px 8px;border-radius:3px}
.compare.ours h4{background:var(--orange)}
.compare .photo{margin-top:8px;height:150px;border-radius:4px}
.compare.general .photo{background:linear-gradient(160deg,#d8d4cc,#a9a49a)}
.compare.ours .photo{background:linear-gradient(160deg,#6b4a33,#2f2219)}
.compare p{font-size:11px;line-height:1.5;margin-top:6px}

/* footer */
.footer{position:absolute;left:0;top:1120px;width:855px;height:80px;background:var(--white);
  display:flex;align-items:center;padding:0 24px;gap:16px;border-top:4px solid var(--orange)}
.footer .brand-name{margin:0;font-size:18px}
.company{font-size:16px;font-weight:700;color:var(--brown);white-space:nowrap}
.address{font-size:10px;color:var(--text);margin-top:2px;white-space:nowrap}
.contact{margin-left:auto;text-align:right}
.contact small{display:block;font-size:10px;color:var(--brown)}
.tel{display:flex;align-items:center;gap:6px;font-size:34px;font-weight:900;color:var(--orange);line-height:1;white-space:nowrap}
.talk{width:96px;height:56px;background:var(--orange);color:var(--white);border-radius:6px;font-size:11px;
  font-weight:700;text-align:center;padding-top:10px;line-height:1.4;flex:none}
</style>
</head>
<body>
<div class="flyer">

  <section class="hero" role="img" aria-label="木の床と大きな窓のある明るいリビングで親子がくつろぐ室内写真">
    <div class="brand-box">
      <div class="brand-tag">白樺工房の新築一戸建</div>
      <div class="brand-name"><span class="mark"></span>ベルタスホーム</div>
      <div class="brand-sub">Beltas Home Company</div>
    </div>
    <p class="hero-note">あんしんして子育てができる環境を考えた家</p>
    <h1 class="title">
      <span class="kanji">炭</span><span class="ni">に</span>
      <span class="wrap">包まれた</span>
      <span class="main"><em>内断熱</em>のお家</span>
    </h1>
  </section>

  <section class="points">
    <h2 class="points-head">炭化コルクの優れた<span class="num">5</span>つの性能</h2>
    <div class="point-row">
      <div class="point"><span class="point-label">Point1</span><div class="point-name">断熱</div>
        <p class="point-text">スペースシャトルの断熱材としても使用されていました。</p></div>
      <div class="point"><span class="point-label">Point2</span><div class="point-name">防虫</div>
        <p class="point-text">スベリンという物質が虫やダニを寄せ付けません。</p></div>
      <div class="point"><span class="point-label">Point3</span><div class="point-name">防音</div>
        <p class="point-text">優れた防音性能と吸音性、衝撃吸収性により音の振動を遮ります。</p></div>
      <div class="point"><span class="point-label">Point4</span><div class="point-name">調湿</div>
        <p class="point-text">空気中の余分な水分を吸収、乾燥時ははき出し結露やカビを防ぎます。</p></div>
      <div class="point"><span class="point-label">Point5</span><div class="point-name">消臭</div>
        <p class="point-text">多孔質な炭の効果で、ペット臭などの嫌なにおいを吸着消臭します。</p></div>
    </div>
  </section>

  <h2 class="air-band">炭化コルク＋漆喰でつくる<em>「空気のおいしい家」</em></h2>

  <div class="diagram" role="img" aria-label="天井と壁に炭化コルクを貼った家の断面イラスト"></div>

  <div class="air-body">
    <p class="air-lead">漆喰と炭の効果で24時間<br><span class="hl">サラッとした空気</span>が365日続きます。</p>
    <p class="air-text">ジメジメした雨の日も室内はカラッと調湿する100%天然素材の断熱材「炭化コルク」。天井と壁に炭化コルクが入っていて、内断熱になっているため<b>夏涼しく、冬暖かい</b>室内にしてくれます。一般的な住宅メーカーはクレナライトと呼ばれる発泡スチロールのような断熱材を天井部分にしか使用していませんが、ベルタスホームは炭化コルクの断熱材を天井と日の当たる壁一面に貼っております。</p>
  </div>

  <section class="bottom">
    <div class="about">
      <h3>炭化コルクとは？</h3>
      <p>コルクの木の樹皮からできています。高温で蒸し焼きにするとコルク自身のヤニで固形化するため、シックハウスの原因となる化学接着剤を使用しない、天然コルク100%の断熱材です。</p>
      <div class="photo" role="img" aria-label="黒い炭化コルクボードの写真"></div>
    </div>
    <div class="compare general">
      <h4>一般的な住宅</h4>
      <div class="photo" role="img" aria-label="天井に白い断熱材を施工した一般的な住宅の写真"></div>
      <p>天井部分のみに発泡系の断熱材を使用しています。</p>
    </div>
    <div class="compare ours">
      <h4>ベルタスホームの住宅</h4>
      <div class="photo" role="img" aria-label="天井と壁一面に炭化コルクを施工した住宅の写真"></div>
      <p>天井と日の当たる壁一面に炭化コルクを貼っています。</p>
    </div>
  </section>

  <footer class="footer">
    <div class="brand-name"><span class="mark"></span>ベルタスホーム</div>
    <div>
      <div class="company">ベルタスホーム株式会社</div>
      <div class="address">〒000-0000 北海道白樺市中央1-2-3</div>
    </div>
    <div class="contact">
      <small>お気軽にお問い合わせください</small>
      <div class="tel">
        <svg width="26" height="26" viewBox="0 0 24 24" aria-hidden="true"><path fill="#e8862a" d="M6.6 10.8a15.1 15.1 0 0 0 6.6 6.6l2.2-2.2a1 1 0 0 1 1-.25 11.4 11.4 0 0 0 3.6.57 1 1 0 0 1 1 1V20a1 1 0 0 1-1 1A17 17 0 0 1 3 4a1 1 0 0 1 1-1h3.5a1 1 0 0 1 1 1c0 1.25.2 2.45.57 3.57a1 1 0 0 1-.25 1z"/></svg>
        0120-345-678
      </div>
    </div>
    <div class="talk">公式トークで<br>友だち登録</div>
  </footer>

</div>
</body>
</html>
```